Business Card Design Project

I help solve problems that people have with real estate, so I buy homes for cash that they no longer want, can't afford, inherited, etc. and fix and sell them or rent them or take over mortgage payments. See website: www.quickhomepurchase-example.com

Industry/Entity Type

Real Estate

Contact Information for Business Card

Not exactly sure. Looking for a design that either is similar to the website www.quickhomepurchase-example.com or that reflects what I do as described below. If it can look a little luxurious to show I can buy the houses for cash and I fix them and sell them, it's a bonus. I seem to like some of the higher end things like foil or black or something that makes it stand out.

Font styles to use
Serif

Requirements
Nice to have
• I seem to like black or clear. I like things to stand out and be different.

```html
<!DOCTYPE html>
<html lang="en">
<head>
<meta charset="utf-8">
<title>Renewed Homes – Business Card</title>
<link rel="stylesheet" href="https://fonts.googleapis.com/css2?family=Tinos:wght@400;700&display=swap">
<style>
  :root {
    --backdrop: #d8cdb9;
    --paper: #ffffff;
    --ink: #141414;
    --green: #8cc63f;
    --green-deep: #4f9a2a;
    --text-light: #f2f2f2;
    --shadow: rgba(0, 0, 0, 0.28);
  }
  * { margin: 0; padding: 0; box-sizing: border-box; }
  html, body {
    width: 1200px;
    height: 780px;
    overflow: hidden;
    background: var(--backdrop);
    font-family: "Tinos", "Times New Roman", serif;
  }
  .canvas {
    position: relative;
    width: 1200px;
    height: 780px;
  }
  .card {
    position: absolute;
    width: 540px;
    height: 308px;
    border-radius: 3px;
    overflow: hidden;
    box-shadow: 0 10px 26px var(--shadow);
  }
  .card-front { left: 70px; top: 110px; background: var(--paper); }
  .card-back { left: 620px; top: 380px; background: var(--ink); }
  .card-art { position: absolute; inset: 0; }

  .brand-name {
    position: absolute;
    color: var(--green-deep);
    font-weight: 700;
    letter-spacing: 1px;
    line-height: 0.95;
    text-transform: uppercase;
  }
  .card-front .brand-name { left: 32px; top: 122px; font-size: 36px; }
  .card-back .brand-name {
    left: 0; right: 0; top: 108px;
    text-align: center;
    font-size: 46px;
    color: var(--green);
  }

  .contact-head {
    position: absolute;
    right: 22px;
    top: 40px;
    text-align: right;
    color: var(--text-light);
  }
  .contact-name {
    font-weight: 700;
    font-size: 19px;
    color: var(--green);
    letter-spacing: 0.5px;
    text-transform: uppercase;
  }
  .contact-role { font-size: 13px; }
  .contact-list {
    position: absolute;
    right: 22px;
    bottom: 34px;
    list-style: none;
    color: var(--text-light);
  }
  .contact-item {
    display: flex;
    align-items: center;
    justify-content: flex-end;
    gap: 7px;
    font-size: 11.5px;
    line-height: 1;
    white-space: nowrap;
    margin-top: 10px;
  }
  .contact-icon { width: 15px; height: 15px; flex: none; }
</style>
</head>
<body>
<main class="canvas">

  <section class="card card-front" aria-label="Business card front">
    <svg class="card-art" viewBox="0 0 540 308" aria-hidden="true">
      <defs>
        <linearGradient id="swoosh-green" x1="0" y1="0" x2="0" y2="1">
          <stop offset="0" stop-color="#b5dc6a"/>
          <stop offset="1" stop-color="#7cbf32"/>
        </linearGradient>
      </defs>
      <path d="M262,0 C300,110 288,220 184,308 H232 C318,220 322,100 288,0 Z" fill="url(#swoosh-green)"/>
      <path d="M288,0 H540 V308 H232 C318,220 322,100 288,0 Z" fill="var(--ink)"/>
    </svg>

    <p class="brand-name">Renewed<br>Homes</p>

    <div class="contact-head">
      <p class="contact-name">Dana Reyes</p>
      <p class="contact-role">CEO</p>
    </div>

    <ul class="contact-list">
      <li class="contact-item">555 555 5555
        <svg class="contact-icon" viewBox="0 0 16 16" aria-hidden="true"><circle cx="8" cy="8" r="7" fill="none" stroke="#8cc63f" stroke-width="1.2"/><rect x="5.5" y="3.8" width="5" height="8.4" rx="1" fill="#8cc63f"/></svg>
      </li>
      <li class="contact-item">info@renewedhomes-example.com
        <svg class="contact-icon" viewBox="0 0 16 16" aria-hidden="true"><circle cx="8" cy="8" r="7" fill="none" stroke="#8cc63f" stroke-width="1.2"/><rect x="4" y="5" width="8" height="6" fill="#8cc63f"/><path d="M4,5 L8,8.5 L12,5" fill="none" stroke="#141414" stroke-width="0.9"/></svg>
      </li>
      <li class="contact-item">www.quickhomepurchase-example.com
        <svg class="contact-icon" viewBox="0 0 16 16" aria-hidden="true"><circle cx="8" cy="8" r="7" fill="none" stroke="#8cc63f" stroke-width="1.2"/><circle cx="8" cy="8" r="4" fill="none" stroke="#8cc63f" stroke-width="1"/><path d="M4,8 H12 M8,4 V12" stroke="#8cc63f" stroke-width="0.9"/></svg>
      </li>
    </ul>
  </section>

  <section class="card card-back" aria-label="Business card back">
    <p class="brand-name">Renewed<br>Homes</p>
  </section>

</main>
</body>
</html>
```